The Willowmere Clinic Flyer Design

The Willowmere Clinic is a new company providing Dietetic services for people with gastrointestinal disorders. The main client base would be people suffering from Irritable Bowel Syndrome. IBS is a collection of symptoms which (will be individual to the suffer) including constipation/diarrhoea/abdominal pain or discomfort/bloating/belching/flatulence/stomach gurgling/reflux/nausea/urgency/incomplete emptying/fatigue/headaches. IBS affects approx 30% of the population. Previous treatments have generally been ineffectual and include medication, hypnotherapy, healthy eating.
Recently it has been found that the FODMAP diet (a diet low in fermentable Carbohydrates) has been effective in 75% of sufferers.
The Low FODMAP diet is complex and it is highly recommended that it is undertaken only under the supervision of a suitably qualified dietitian. Treatment is available within the QRV but is usually accessible only following consultation with a Gastroenterologist. Most GP's have never heard of this treatment as the research was only published in 2009 in Australia and is yet to filter through to the general practitioner. The Willowmere Clinic is the only clinic in the UK offering dietetic lead specialist services.
I am a member of the ZLO and MVRT (logos provided)
The flyer would be double sided, informing the patient of all the self help steps they could take if they have IBS then recommending that they contact The Willowmere Clinic for specialist advice.
Self Help: Healthy eating, regular meals, good intake of non caffeinated non alcoholic non fizzy drinks, regular exercise, stress management.
The flyer would be left in GP surgeries, Health centres, holistic therapy centres, or through doors.
Target Market(s)
Majority female aged 20-50, able to pay for private services
Industry/Entity Type
Clinic
Look and feel
Each slider illustrates characteristics of the customer's brand and the style your logo design should communicate.

```html
<!DOCTYPE html>
<html lang="en">
<head>
<meta charset="utf-8">
<title>The Willowmere Clinic – IBS Flyer</title>
<link href="https://fonts.googleapis.com/css2?family=Roboto+Condensed:wght@300;400;700&family=Arimo:wght@400;700&display=swap" rel="stylesheet">
<style>
  :root {
    --navy: #004f74;
    --ink: #0b4f74;
    --sky: #1a7fb0;
    --pale: #a9d4ea;
    --mist: #8fb6cc;
    --body: #5d87a0;
    --card: #a3c3d6;
    --card-text: #5e7f95;
    --bg: #f2f7fa;
    --white: #ffffff;
  }
  * { margin: 0; padding: 0; box-sizing: border-box; }
  html, body { width: 1200px; height: 851px; overflow: hidden; background: var(--bg); }
  .flyer {
    position: relative; width: 1200px; height: 851px; overflow: hidden;
    background: radial-gradient(ellipse at 30% 60%, #ffffff 0%, var(--bg) 70%);
    font-family: "Arimo", Arial, sans-serif;
  }
  .abs { position: absolute; }
  .cond { font-family: "Roboto Condensed", "Arial Narrow", sans-serif; }

  /* Top band */
  .band { left: 0; top: 0; width: 1200px; height: 272px; background: var(--navy); }
  .figure-mark { background: var(--white); border-radius: 14px 14px 3px 3px; }
  .self-help-title { left: 195px; top: 78px; font-size: 43px; font-weight: 700; color: var(--white); letter-spacing: 2px; line-height: 1; }
  .brace { left: 250px; top: 130px; }
  .self-help-text { left: 70px; width: 422px; top: 159px; text-align: center; font-size: 17px; line-height: 21.5px; color: var(--white); }
  .next-arrow { left: 584px; top: 95px; }
  .next-note { left: 546px; width: 140px; top: 166px; text-align: center; font-size: 13px; color: var(--mist); }
  .contact-title { left: 791px; top: 75px; font-size: 35px; font-weight: 700; color: var(--white); letter-spacing: 2.5px; line-height: 1; }
  .contact-list { left: 791px; top: 119px; list-style: none; font-size: 19px; line-height: 24.5px; color: var(--pale); font-weight: 300; }

  /* Lower section */
  .section-title { font-size: 43px; font-weight: 400; color: var(--ink); line-height: 1; letter-spacing: 0.5px; }
  .why-title { left: 70px; top: 309px; }
  .know-title { left: 711px; top: 309px; }
  .divider-v { left: 636px; top: 322px; width: 1.5px; height: 487px; background: var(--ink); opacity: .8; }
  .divider-h { left: 48px; top: 540px; width: 551px; height: 1.5px; background: var(--ink); opacity: .8; }

  .patient-figure { left: 110px; top: 382px; width: 50px; height: 131px; background: var(--ink); border-radius: 20px 20px 4px 4px; }
  .stat-big { font-size: 59px; color: var(--ink); line-height: 1; font-weight: 400; }
  .stat-75 { left: 166px; top: 377px; }
  .stat-patients { left: 168px; top: 431px; font-size: 28px; color: var(--sky); line-height: 1; letter-spacing: 0.5px; }
  .stat-note { left: 168px; top: 464px; width: 112px; font-size: 13px; line-height: 16.5px; color: var(--sky); text-align: justify; text-align-last: justify; }

  .clipboard { left: 361px; top: 389px; width: 83px; height: 109px; background: var(--ink); border-radius: 6px; }
  .stat-within { left: 448px; top: 393px; width: 84px; font-size: 11px; line-height: 14px; color: var(--sky); text-align: justify; text-align-last: justify; }
  .stat-weeks-num { left: 448px; top: 424px; }
  .stat-weeks { left: 449px; top: 474px; font-size: 28px; color: var(--sky); line-height: 1; letter-spacing: 0.5px; }

  .include-title { left: 48px; width: 551px; top: 581px; text-align: center; font-size: 33px; color: var(--ink); line-height: 1; }
  .step { top: 653px; width: 164px; height: 141px; background: var(--card); border-radius: 18px; }
  .step-1 { left: 63px; } .step-2 { left: 242px; } .step-3 { left: 421px; }
  .step-badge { position: absolute; left: 50%; top: 0; width: 44px; height: 44px; margin: -22px 0 0 -22px; background: var(--navy); transform: rotate(45deg); }
  .step-num { position: absolute; left: 0; width: 100%; top: -17px; text-align: center; font-size: 29px; font-weight: 700; color: var(--white); line-height: 34px; }
  .step-text { position: absolute; left: 10px; right: 10px; top: 38px; text-align: center; font-size: 13.5px; line-height: 17px; color: var(--card-text); }

  .facts { left: 711px; top: 374px; width: 410px; font-size: 17px; line-height: 21.5px; color: var(--body); text-align: justify; }
  .facts p { margin-bottom: 21.5px; }
  .facts .claim { font-weight: 700; color: #4e7a93; text-align: left; }
</style>
</head>
<body>
<main class="flyer">
  <section class="band abs" aria-label="Self help">
  </section>
  <div class="figure-mark abs" style="left:151px;top:48px;width:30px;height:71px;" role="img" aria-label="Standing person pictogram"></div>
  <h1 class="self-help-title cond abs">SELF HELP</h1>
  <svg class="brace abs" width="58" height="16" viewBox="0 0 58 16" aria-hidden="true">
    <path d="M1 1 Q1 7 10 7 L23 7 Q29 7 29 14 Q29 7 35 7 L48 7 Q57 7 57 1" fill="none" stroke="#ffffff" stroke-width="2.5"/>
  </svg>
  <p class="self-help-text abs">Healthy eating, regular meals, good intake of non caffeinated non alcoholic non fizzy drinks, regular exercise, stress management</p>
  <svg class="next-arrow abs" width="63" height="50" viewBox="0 0 63 50" aria-hidden="true">
    <path d="M0 15 H37 V0 L63 25 L37 50 V35 H0 Z" fill="#7fa9c2"/>
  </svg>
  <p class="next-note abs">if this doesn't help</p>
  <h2 class="contact-title cond abs">PLEASE CONTACT US</h2>
  <ul class="contact-list cond abs">
    <li>Tel: +44 555 0192</li>
    <li>Email: hello@willowmereclinic.com</li>
    <li>Website: www.willowmereclinic.com</li>
  </ul>

  <h2 class="section-title why-title cond abs">WHY CHOOSE OUR SERVICES?</h2>
  <div class="patient-figure abs" role="img" aria-label="Person pictogram"></div>
  <div class="stat-big stat-75 cond abs">75%</div>
  <div class="stat-patients cond abs">Patients</div>
  <p class="stat-note abs">clinically proven work up in dietary treatment</p>
  <div class="clipboard abs" role="img" aria-label="Clipboard checklist pictogram"></div>
  <p class="stat-within abs">Results can be seen within</p>
  <div class="stat-big stat-weeks-num cond abs">1-2</div>
  <div class="stat-weeks cond abs">weeks</div>

  <div class="divider-h abs"></div>
  <div class="divider-v abs"></div>

  <h2 class="include-title cond abs">WHAT’S INCLUDE IN THE TREATMENT?</h2>
  <div class="step step-1 abs">
    <span class="step-badge"></span><span class="step-num cond">1</span>
    <p class="step-text">1 hour teaching session on the elimination phase, phone and e-mail support</p>
  </div>
  <div class="step step-2 abs">
    <span class="step-badge"></span><span class="step-num cond">2</span>
    <p class="step-text">1 hour appointment to teach the reintroduction phase</p>
  </div>
  <div class="step step-3 abs">
    <span class="step-badge"></span><span class="step-num cond">3</span>
    <p class="step-text">1 hour appointment to assess nutritional adequacy of the diet</p>
  </div>

  <h2 class="section-title know-title cond abs">DID YOU KNOW?</h2>
  <div class="facts abs">
    <p>IBS affects approx 30% of the population. Previous treatments have generally been ineffectual and include medication, hypnotherapy, healthy eating.</p>
    <p>Recently it has been found that the FODMAP diet (a diet low in fermentable Carbohydrates) has been effective in 75% of sufferers.</p>
    <p>The Low FODMAP diet is complex and it is highly recommended that it is undertaken only under the supervision of a suitably qualified dietitian. Treatment is available within the QRV but is usually accessible only following consultation with a Gastroenterologist. Most GP's have never heard of this treatment as the research was only published in 2009 in Australia and is yet to filter through to the general practitioner.</p>
    <p class="claim">The Willowmere Clinic is the only clinic in the UK offering dietetic lead specialist services.</p>
  </div>
</main>
</body>
</html>
```